Crate of Play creation for Kids Classic Games for Outdoor Play

We need to design a Crate of Play (soft paper box or carton box) that will contain classic outdoor-old school kids games (teetotums, jumping ropes etc.). I am thinking the design to have a vintage feeling with a modern touch though.
If you come up with some thing different, its welcome..!
The box will have 7 compartments(dividers) inside each representing a game. The Box will have the following dimensions:
60cm(L)x30cm(W)x10cm(H).
Out of the 7 compartments, we need to have one long side divider (compartment) for a ball with its pump (20cm x 30 cm x 10cm) and 6 smaller compartments of 13cm x 15cm x 10cm.
We are thinking - but are not sure - if at the bottom of each compartment (game) there should be a painting/sketch showcasing the game.
We just thought we could call this project "The chest of pastimes" or "Crate of Play" and include as well a small book which will explain how the games are played. Ideas are welcome on the booklet too.
**UPDATE: I have just found an EXCELLENT design that i want to follow. Please see attached and go with it.
Many many thanks!
Parents who will remember their youth and the games they played in the neighborhood, hence they will buy for their kids as a gift.
School

```html
<!DOCTYPE html>
<html lang="en">
<head>
<meta charset="utf-8">
<title>Crate of Play – Box Dieline</title>
<link rel="stylesheet" href="https://fonts.googleapis.com/css2?family=Stardos+Stencil:wght@700&family=Big+Shoulders+Stencil+Text:wght@800&display=swap">
<style>
  :root {
    --paper: #ffffff;
    --kraft: #e9d8a9;
    --sky: #89d4f5;
    --cream: #f7f0da;
    --white: #ffffff;
    --cut-line: #8a8a8a;
    --ink: #222222;
  }
  html, body {
    margin: 0;
    padding: 0;
    width: 1200px;
    height: 789px;
    overflow: hidden;
    background: var(--paper);
  }
  .dieline { display: block; width: 1200px; height: 789px; }
  .flap-white { fill: var(--white); stroke: var(--cut-line); stroke-width: 0.6; }
  .panel { fill: var(--kraft); stroke: var(--cut-line); stroke-width: 0.8; }
  .side-strip { fill: var(--sky); }
  .panel-frame { fill: none; stroke: var(--cream); stroke-width: 4; }
  .brand-name {
    font-family: "Stardos Stencil", "Arial Black", sans-serif;
    font-weight: 700;
    font-size: 50px;
    letter-spacing: 1px;
    fill: var(--sky);
  }
  .illustration-large { fill: var(--sky); }
  .illustration-small { fill: var(--white); }
  .info-card { fill: var(--sky); }
  .info-copy {
    font-family: Arial, Helvetica, sans-serif;
    font-size: 3.3px;
    fill: var(--white);
  }
  .section-caption {
    font-family: Arial, Helvetica, sans-serif;
    font-size: 5px;
    fill: var(--ink);
  }
  .compartment { fill: var(--kraft); stroke: var(--cut-line); stroke-width: 0.8; }
  .compartment-tile { fill: var(--sky); }
  .compartment-label {
    font-family: "Big Shoulders Stencil Text", "Arial Narrow", sans-serif;
    font-weight: 800;
    font-size: 17px;
    letter-spacing: 0.5px;
    fill: var(--white);
  }
</style>
</head>
<body>
<svg class="dieline" viewBox="0 0 1350 887" xmlns="http://www.w3.org/2000/svg">

  <g class="box-net">
    <polygon class="flap-white" points="167,70 177,44 701,44 711,70"/>
    <polygon class="flap-white" points="76,163 50,168 50,428 76,433"/>
    <polygon class="flap-white" points="803,163 829,168 829,428 803,433"/>
    <polygon class="flap-white" points="167,797 711,797 701,851 177,851"/>

    <rect class="panel" x="167" y="70" width="544" height="91"/>
    <rect class="panel" x="76" y="161" width="91" height="273"/>
    <rect class="panel" x="167" y="161" width="544" height="273"/>
    <rect class="panel" x="711" y="161" width="92" height="273"/>
    <rect class="panel" x="167" y="434" width="544" height="91"/>
    <rect class="panel" x="167" y="525" width="544" height="272"/>

    <rect class="side-strip" x="87" y="192" width="66" height="211"/>
    <rect class="side-strip" x="725" y="192" width="66" height="211"/>
    <rect class="illustration-small" x="80" y="328" width="80" height="74" rx="18" role="img" aria-label="Small spinning top illustration"/>
    <rect class="illustration-small" x="716" y="194" width="82" height="74" rx="18" role="img" aria-label="Small spinning top illustration"/>

    <rect class="panel-frame" x="202" y="192" width="471" height="209" rx="8"/>
    <text class="brand-name" x="216" y="252">CRATE</text>
    <text class="brand-name" x="216" y="304">OF PLAY</text>
    <rect class="illustration-large" x="478" y="168" width="184" height="250" rx="40" role="img" aria-label="Large spinning top illustration"/>

    <rect class="panel-frame" x="202" y="557" width="471" height="208" rx="8"/>
    <rect class="info-card" x="208" y="563" width="157" height="195" rx="10"/>
    <text class="info-copy">
      <tspan x="232" y="589">Every box holds seven classic games for sunny days outside.</tspan>
      <tspan x="232" y="594">Pick a game, call your friends and play like we once did.</tspan>
      <tspan x="232" y="599">The booklet inside explains the rules step by step.</tspan>
      <tspan x="232" y="607">Spin the top, skip the rope and roll the marbles on the path.</tspan>
      <tspan x="232" y="612">Pump the ball, mark a goal and let the match begin.</tspan>
      <tspan x="232" y="617">Share the fun with family and keep every piece in place.</tspan>
    </text>
  </g>

  <g class="inside-tray">
    <text class="section-caption" x="759" y="519">INSIDE OF BOX</text>

    <rect class="compartment" x="759" y="526" width="181" height="272"/>
    <rect class="compartment" x="940" y="526" width="121" height="136"/>
    <rect class="compartment" x="1061" y="526" width="122" height="136"/>
    <rect class="compartment" x="1183" y="526" width="121" height="136"/>
    <rect class="compartment" x="940" y="662" width="121" height="136"/>
    <rect class="compartment" x="1061" y="662" width="122" height="136"/>
    <rect class="compartment" x="1183" y="662" width="121" height="136"/>

    <rect class="compartment-tile" x="771" y="538" width="157" height="248" rx="12"/>
    <rect class="compartment-tile" x="953" y="538" width="96" height="113" rx="9"/>
    <rect class="compartment-tile" x="1074" y="538" width="96" height="113" rx="9"/>
    <rect class="compartment-tile" x="1195" y="538" width="96" height="113" rx="9"/>
    <rect class="compartment-tile" x="953" y="674" width="96" height="113" rx="9"/>
    <rect class="compartment-tile" x="1074" y="674" width="96" height="113" rx="9"/>
    <rect class="compartment-tile" x="1195" y="674" width="96" height="113" rx="9"/>

    <text class="compartment-label" transform="translate(804 648) rotate(-90)">BALL &amp; PUMP</text>
    <text class="compartment-label" transform="translate(985 617) rotate(-90)">MARBLES</text>
    <text class="compartment-label" transform="translate(1106 614) rotate(-90)">NO NAME</text>
    <text class="compartment-label" transform="translate(1227 620) rotate(-90)">TEETOTUM</text>
    <text class="compartment-label" transform="translate(985 751) rotate(-90)">NO NAME</text>
    <text class="compartment-label" transform="translate(1096 752) rotate(-90)">JUMPING</text>
    <text class="compartment-label" transform="translate(1114 741) rotate(-90)">ROPE</text>
    <text class="compartment-label" transform="translate(1227 751) rotate(-90)">NO NAME</text>
  </g>
</svg>
</body>
</html>
```